Photographer Card

I'm currently doing freelance photography and i need a creative design name card especially when i attend events.
I require a design that makes a STATEMENT.
Simple, elegant and nothing like the usual name cards ive seen around (Example: with a camera/tripod etc in the design).

Photographer: Dorian VP
Mobile: +65 84126957
E-mail: Dorian.VP.Photography@mailvista.net
Facebook: www.friendlane.net/dorian.vp.photography

Thanks for your time and hope it will turn out well! :)
Updates

Thanks for all your inputs!

Im liking the cursive feel.

Id prefer not to include the title "freelance"  :)

Also, im looking for a logo to establish myself

http://www.artmosaic.net/art/Cotton-Business-Card-583021746

Hi all! Thanks for the designs

"Capturing magical moments"
"Capturing magical moments that are gone forever"

Back design can be in big font "look HERE"

Maybe with focusing box 

Names can be played with horizontal and vertical.

Industry/Entity Type

Camera

Font styles to use
Script

```html
<!DOCTYPE html>
<html lang="en">
<head>
<meta charset="utf-8">
<title>Dorian VP Photography – Business Card</title>
<link rel="stylesheet" href="https://fonts.googleapis.com/css2?family=Josefin+Sans:wght@300;600&display=swap">
<style>
  :root {
    --backdrop: #e8e5da;
    --card-light: #f4f4f4;
    --card-light-edge: #dcdcdc;
    --card-dark: #1c1c1c;
    --ink: #2a2a2a;
    --ink-soft: #555555;
    --bracket-dark: #6a6a6a;
    --bracket-light: #ffffff;
    --mark-light: #e6e6e6;
    --icon-fill: #2b2b2b;
  }
  * { box-sizing: border-box; margin: 0; padding: 0; }
  html, body {
    width: 1200px; height: 716px; overflow: hidden;
    background: var(--backdrop);
  }
  .canvas {
    position: relative; width: 1200px; height: 716px;
    display: flex; align-items: center; justify-content: center; gap: 40px;
  }
  .card {
    position: relative; width: 540px; height: 309px;
    box-shadow: 0 10px 24px rgba(0,0,0,.14);
  }
  .card--front {
    background: linear-gradient(160deg, #ffffff 0%, var(--card-light) 60%, var(--card-light-edge) 100%);
  }
  .card--back { background: var(--card-dark); }

  .bracket {
    position: absolute; width: 34px; height: 22px;
    border-style: solid; border-width: 0;
  }
  .card--front .bracket { border-color: var(--bracket-dark); }
  .card--back .bracket { border-color: var(--bracket-light); }
  .bracket--tl { top: 30px; left: 36px; border-top-width: 2px; border-left-width: 2px; }
  .bracket--tr { top: 30px; right: 36px; border-top-width: 2px; border-right-width: 2px; }
  .bracket--bl { bottom: 30px; left: 36px; border-bottom-width: 2px; border-left-width: 2px; }
  .bracket--br { bottom: 30px; right: 36px; border-bottom-width: 2px; border-right-width: 2px; }

  /* Front */
  .front-name {
    position: absolute; top: 74px; left: 0; right: 0; text-align: center;
  }
  .front-name__person {
    display: block;
    font-family: "Josefin Sans", sans-serif; font-weight: 300;
    font-size: 40px; color: var(--ink-soft); line-height: 1;
  }
  .front-name__role {
    display: block; margin-top: 2px; padding-left: 60px;
    font-family: "Josefin Sans", sans-serif; font-weight: 600;
    font-size: 17px; color: var(--ink);
  }
  .contact-list {
    position: absolute; left: 62px; top: 166px; list-style: none;
  }
  .contact-list__item {
    display: flex; align-items: center; gap: 10px; margin-bottom: 9px;
    font-family: "Josefin Sans", sans-serif; font-weight: 300;
    font-size: 16px; color: var(--ink);
  }
  .contact-list__icon { width: 16px; height: 16px; flex: none; }

  /* Back */
  .back-mark {
    position: absolute; top: 0; bottom: 0; left: 0; right: 0;
    display: flex; align-items: center; justify-content: center; gap: 16px;
  }
  .back-mark__dot {
    width: 26px; height: 26px; border-radius: 50%;
    background: var(--mark-light); flex: none;
  }
  .back-mark__name {
    font-family: "Josefin Sans", sans-serif; font-weight: 300;
    font-size: 38px; color: var(--mark-light); letter-spacing: 1px; line-height: 1;
  }
</style>
</head>
<body>
<main class="canvas">
  <section class="card card--front" aria-label="Business card front">
    <span class="bracket bracket--tr"></span>
    <span class="bracket bracket--bl"></span>
    <span class="bracket bracket--br"></span>
    <h1 class="front-name">
      <span class="front-name__person">Dorian VP</span>
      <span class="front-name__role">Photographer</span>
    </h1>
    <ul class="contact-list">
      <li class="contact-list__item">
        <svg class="contact-list__icon" viewBox="0 0 16 16" aria-hidden="true">
          <circle cx="8" cy="8" r="8" fill="var(--icon-fill)"/>
          <path d="M5.6 4.2c.3-.2.6-.1.8.2l.7 1.2c.1.3.1.6-.2.8l-.4.3c.3.8 1 1.6 1.8 2l.3-.4c.2-.3.5-.3.8-.2l1.2.7c.3.2.4.5.2.8l-.4.7c-.3.5-1 .6-1.6.3-1.8-.9-3.1-2.3-3.8-4-.2-.6 0-1.2.5-1.5z" fill="#fff"/>
        </svg>
        +65 84126957
      </li>
      <li class="contact-list__item">
        <svg class="contact-list__icon" viewBox="0 0 16 16" aria-hidden="true">
          <circle cx="8" cy="8" r="8" fill="var(--icon-fill)"/>
        </svg>
        dorian.vp.photography
      </li>
      <li class="contact-list__item">
        <svg class="contact-list__icon" viewBox="0 0 16 16" aria-hidden="true">
          <circle cx="8" cy="8" r="8" fill="var(--icon-fill)"/>
        </svg>
        Dorian.VP.Photography@mailvista.net
      </li>
    </ul>
  </section>

  <section class="card card--back" aria-label="Business card back">
    <span class="bracket bracket--tl"></span>
    <span class="bracket bracket--tr"></span>
    <span class="bracket bracket--bl"></span>
    <span class="bracket bracket--br"></span>
    <div class="back-mark">
      <span class="back-mark__dot"></span>
      <span class="back-mark__name">Dorian VP Photography</span>
    </div>
  </section>
</main>
</body>
</html>
```